Maple's Pantry Home Page Design

Hello ArtHivePro -

I am looking for a home page design for an Indian Food Grocery ecommerce site with a store in Boulder, CO. This design request is just for the home page (http://maplespantry.com/), including new design, font, layout and emblem/word mark logo.

What: Maple's Pantry (spices, lentils, rice, frozen foods, etc.)

Desired Color Scheme: Warm, earth tones (red, orange, yellow), that remind the guest of Indian Spices

Tone: This is an Indian-American family owned, small business catering imported Indian foods and spices to a primary market of Indian-Americans and a secondary market of Indian food/spice lovers.

Themes to communicate: Indian, family owned, food

Sample Websites: http://www.brivantfare.com/, http://www.tolvacart.com/, http://www.quenlarmart.com/

Please feel free to reach out with any questions. Thank you.

Target Market(s)

Indian-Americans (1st and 2nd Generation)

Industry/Entity Type

Small Business

Requirements
Must have
• Final Design must be delivered in layered PSD file with all fonts and licenses used.

```html
<!DOCTYPE html>
<html lang="en">
<head>
<meta charset="utf-8">
<title>Maple's Pantry – Home</title>
<link rel="stylesheet" href="https://fonts.googleapis.com/css2?family=PT+Sans:ital,wght@0,400;0,700;1,400&family=Gelasio:ital,wght@0,400;0,600;1,400&display=swap">
<style>
:root{
  --hero-top:#f0512c;
  --hero-mid:#e84a22;
  --hero-bot:#c93a10;
  --cream:#fdf5c8;
  --page-bg:#e8e6e8;
  --panel:#ffffff;
  --red:#d6401a;
  --red-dark:#b8300c;
  --btn-red:#c7340f;
  --orange-btn:#f06a10;
  --yellow-btn:#fbb900;
  --yellow:#ffd200;
  --text:#333333;
  --muted:#555555;
  --rule:#dddddd;
  --footer:#b8310c;
  --footer-dark:#a4280a;
  --white:#ffffff;
}
*{margin:0;padding:0;box-sizing:border-box}
html,body{width:1200px;height:2299px;overflow:hidden}
body{position:relative;background:var(--page-bg);font-family:"PT Sans",Arial,sans-serif;color:var(--text)}
.abs{position:absolute}

/* header / hero */
.hero{left:0;top:0;width:1200px;height:662px;background:linear-gradient(180deg,var(--hero-top) 0%,var(--hero-mid) 55%,var(--hero-bot) 100%)}
.top-band{left:0;top:0;width:1200px;height:8px;background:var(--cream)}
.hero-edge{left:0;top:656px;width:1200px;height:6px;border-top:2px dashed #f58a5e}
.logo{left:54px;top:64px;font-size:35px;font-weight:700;color:var(--cream);letter-spacing:.3px;line-height:42px}
.slogan{left:172px;top:104px;font-size:14px;color:#fde3d4}
.cart{left:964px;top:46px;font-size:13px;color:#fde3d4;display:flex;align-items:center;gap:6px}
.cart b{color:var(--white);font-size:15px}
.nav{left:426px;top:84px;width:721px;height:57px;border:2px solid #f7855a;border-radius:6px;background:linear-gradient(180deg,#e3461c,#d33c14);display:flex;align-items:center;justify-content:space-around;padding:0 20px}
.nav a{color:var(--white);text-decoration:none;font-size:18px;flex:1;text-align:center;border-left:2px dotted #f7a07c;line-height:30px}
.nav a:first-child{border-left:0}
.hero-title{left:87px;top:226px;width:420px;font-family:"Gelasio",Georgia,serif;font-weight:400;font-size:32px;line-height:40px;color:var(--white)}
.hero-sub{left:89px;top:314px;font-family:"Gelasio",Georgia,serif;font-size:22px;color:var(--white)}
.hero-copy{left:89px;top:352px;width:375px;font-size:13px;line-height:20px;font-style:italic;color:#fde0d2}
.btn{display:inline-block;text-decoration:none;font-weight:700;text-align:center}
.btn-signup{left:87px;top:458px;width:125px;height:40px;line-height:40px;background:var(--yellow);color:var(--red-dark);border-radius:3px;font-size:16px}
.btn-learn{left:221px;top:458px;width:125px;height:40px;line-height:40px;background:var(--white);color:var(--red-dark);border-radius:3px;font-size:16px}
.frame{background:var(--white);padding:9px;box-shadow:0 4px 12px rgba(0,0,0,.35)}
.frame div{width:100%;height:100%}
.frame-back{left:600px;top:185px;width:505px;height:360px;transform:rotate(-3deg)}
.frame-back div{background:linear-gradient(135deg,#6a4a2c,#b08250)}
.frame-front{left:560px;top:200px;width:540px;height:375px;transform:rotate(-4deg)}
.frame-front div{background:radial-gradient(circle at 45% 45%,#f3eeee 0%,#e6dada 45%,#c7343e 80%,#8d1a24 100%)}
.arrow{top:328px}
.dots{left:574px;top:632px;display:flex;gap:6px}
.dots i{width:12px;height:12px;border-radius:50%;background:#fbe7a8;display:block}

/* main panel */
.panel{left:49px;top:662px;width:1102px;height:1196px;background:var(--panel)}
.ribbon{left:74px;top:699px}
.ribbon-label{left:98px;top:712px;font-family:"Gelasio",Georgia,serif;font-size:20px;color:var(--white);white-space:nowrap}
.products{left:81px;top:777px;width:1040px;display:flex;justify-content:space-between}
.product{width:190px}
.product .ph{width:190px;height:190px}
.product p{margin-top:20px;font-family:"Gelasio",Georgia,serif;font-style:italic;font-size:14px;line-height:20px;color:var(--muted)}
.pill{display:inline-block;border-radius:16px;color:var(--white);text-decoration:none;font-family:"Gelasio",Georgia,serif;text-align:center}
.pill-sm{margin-top:14px;width:86px;height:29px;line-height:29px;font-size:12px;background:var(--btn-red)}
.rule{left:85px;width:1036px;height:1px;background:var(--rule)}
.h2{font-family:"Gelasio",Georgia,serif;font-weight:400;font-size:22px;color:var(--red)}
.welcome-title{left:84px;top:1122px}
.welcome{left:89px;top:1165px;width:680px;color:var(--red);font-size:12px;line-height:19px}
.welcome .lead{font-size:15px;font-weight:700;margin-bottom:12px}
.welcome p{margin-bottom:10px}
.pill-or{width:86px;height:30px;line-height:30px;font-size:13px;background:var(--orange-btn)}
.viewall-1{left:83px;top:1405px}
.best-title{left:802px;top:1124px;font-size:20px}
.thumbs{left:802px;top:1162px;width:320px;display:grid;grid-template-columns:154px 152px;gap:14px;row-gap:15px}
.thumb{height:110px;border:1px solid #e2e2e2;padding:5px;background:var(--white)}
.thumb div{width:100%;height:100%}
.viewall-2{left:812px;top:1411px}
.col{width:314px}
.col h3{font-family:"Gelasio",Georgia,serif;font-weight:400;font-size:20px;color:var(--red);margin-bottom:10px}
.col .ph{width:314px;height:130px;border-radius:3px}
.col .t{margin-top:14px;font-size:13px;font-weight:700;color:#222}
.col .b{margin-top:8px;font-size:13px;line-height:20px;color:var(--muted)}
.col-1{left:89px;top:1488px}
.col-2{left:455px;top:1488px}
.col-3{left:808px;top:1488px;width:314px}
.quote .t{font-style:italic;font-weight:700;font-size:12.5px;color:#222;margin-top:0}
.quote .b{font-style:italic;font-size:12.5px;line-height:20px;color:var(--muted);margin-top:6px}
.quote .by{text-align:right;font-size:11.5px;font-weight:700;color:#333;margin-top:4px;margin-bottom:28px}
.pill-y{width:88px;height:30px;line-height:30px;font-size:13px;background:var(--yellow-btn)}
.rm-1{left:89px;top:1788px}
.rm-2{left:457px;top:1788px}
.rm-3{left:812px;top:1788px}

/* footer */
.footer{left:0;top:1858px;width:1200px;height:441px;background:linear-gradient(180deg,var(--footer) 0%,var(--footer-dark) 100%)}
.fcol{top:1900px;list-style:none}
.fcol li{color:var(--white);font-size:14px;line-height:32px;padding-left:16px;position:relative}
.fcol li::before{content:"";position:absolute;left:0;top:13px;border-left:5px solid #f58a5e;border-top:3px solid transparent;border-bottom:3px solid transparent}
.ground{left:0;top:2130px}
.toy-blocks{left:187px;top:2148px;width:74px;height:66px;border-radius:6px;background:linear-gradient(135deg,#e8493a,#3b8ee0 50%,#f5c52c)}
.toy-horse{left:874px;top:2116px;width:138px;height:106px;border-radius:40px 40px 20px 20px;background:linear-gradient(180deg,#f3f0ea 0%,#f0b23a 55%,#7cc63e 100%)}
.copy{left:55px;top:2256px;font-size:12px;color:#c9471c}
.legal{left:995px;top:2256px;font-size:12px;color:#c9471c}
</style>
</head>
<body>

<header class="abs hero"></header>
<div class="abs top-band"></div>
<svg class="abs" style="left:420px;top:8px" width="740" height="90" viewBox="0 0 740 90" aria-hidden="true" fill="none" stroke="#f7855a" stroke-width="2">
  <path d="M16 88 C4 60 4 20 20 0"/><path d="M720 88 C734 60 734 20 718 0"/>
</svg>
<div class="abs hero-edge"></div>

<div class="abs logo">Maple's Pantry</div>
<div class="abs slogan">slogan goes here</div>

<div class="abs cart">
  <svg width="20" height="16" viewBox="0 0 20 16" aria-hidden="true" fill="none" stroke="#fff" stroke-width="1.6"><path d="M1 1h3l2 9h11l2-7H5"/><circle cx="8" cy="14" r="1.3"/><circle cx="15" cy="14" r="1.3"/></svg>
  <span>Shopping Cart: <b>0 itmes</b></span>
</div>

<nav class="abs nav">
  <a href="#">Main</a><a href="#">About</a><a href="#">Products</a><a href="#">Shop</a><a href="#">Blog</a><a href="#">Order</a><a href="#">Contact</a>
</nav>

<h1 class="abs hero-title">Maple's Pantry Puch Line goes here..</h1>
<div class="abs hero-sub">your tittle line goes here</div>
<p class="abs hero-copy">Nulla rhoncus dictum metus. Curabitur tristique mi condimentum orci. Phasellus pellentesque aliquam enim. Proin dui lectus, cursus eu, mattis laoreet, viverra sit amet, quam. Curabitur vel dolor ultrices ipsum dictum tristique. Praesent vitae lacus.</p>
<a class="abs btn btn-signup" href="#">Sign up Now</a>
<a class="abs btn btn-learn" href="#">Learn More</a>

<div class="abs frame frame-back"><div role="img" aria-label="Photo of spices and dried goods in baskets"></div></div>
<div class="abs frame frame-front"><div role="img" aria-label="Photo of vanilla ice cream scoops with raspberry sauce in a glass bowl"></div></div>

<svg class="abs arrow" style="left:14px" width="34" height="68" viewBox="0 0 34 68" aria-hidden="true"><path d="M30 4 L6 34 L30 64" fill="none" stroke="#fff" stroke-width="6" stroke-linecap="round" stroke-linejoin="round"/></svg>
<svg class="abs arrow" style="left:1152px" width="34" height="68" viewBox="0 0 34 68" aria-hidden="true"><path d="M4 4 L28 34 L4 64" fill="none" stroke="#fff" stroke-width="6" stroke-linecap="round" stroke-linejoin="round"/></svg>
<div class="abs dots"><i></i><i></i><i></i><i></i></div>

<main class="abs panel"></main>

<svg class="abs ribbon" width="236" height="54" viewBox="0 0 236 54" aria-hidden="true">
  <path d="M0 0 H236 L222 27 L236 54 H0 Z" fill="#c93a10"/>
  <path d="M0 0 H8 V54 H0 Z" fill="#a52a08"/>
</svg>
<div class="abs ribbon-label">Featured Products</div>

<section class="abs products">
  <div class="product"><div class="ph" role="img" aria-label="Photo of packaged sausages" style="background:linear-gradient(135deg,#5a3018,#b5561e 60%,#e8c27a)"></div><p>Lorem ipsum dolor sit amet, consectetuer</p><a class="pill pill-sm" href="#">View Details</a></div>
  <div class="product"><div class="ph" role="img" aria-label="Photo of sliced salami" style="background:linear-gradient(135deg,#4a2a20,#b0504a 55%,#e8dcd0)"></div><p>Lorem ipsum dolor sit amet, consectetuer</p><a class="pill pill-sm" href="#">View Details</a></div>
  <div class="product"><div class="ph" role="img" aria-label="Photo of fresh apricots" style="background:radial-gradient(circle at 40% 40%,#f7a74a,#e0701c 60%,#8a3a10)"></div><p>Lorem ipsum dolor sit amet, consectetuer</p><a class="pill pill-sm" href="#">View Details</a></div>
  <div class="product"><div class="ph" role="img" aria-label="Photo of cosmetics and powder compact" style="background:linear-gradient(135deg,#e8e2d6,#c8b79a 50%,#6a6a62)"></div><p>Lorem ipsum dolor sit amet, consectetuer</p><a class="pill pill-sm" href="#">View Details</a></div>
  <div class="product"><div class="ph" role="img" aria-label="Photo of a steel cooking pot with vegetables" style="background:linear-gradient(180deg,#fafafa,#d8d8dc 60%,#b8b4b8)"></div><p>Lorem ipsum dolor sit amet, consectetuer</p><a class="pill pill-sm" href="#">View Details</a></div>
</section>

<div class="abs rule" style="top:1098px"></div>

<h2 class="abs h2 welcome-title">Welcome to Our Website Mainpage..</h2>
<section class="abs welcome">
  <p class="lead">Lorem ipsum dolor sit amet, consectetuer adipiscing elit. Nam cursus.</p>
  <p>Mauris vel lacus vitae felis vestibulum volutpat. Etiam est nunc, venenatis in, tristique eu, imperdiet ac, nisl. Cum sociis natoque penatibus et magnis dis parturient montes, nascetur ridiculus mus. In iaculis facilisis massa. Etiam eu urna.</p>
  <p>Mauris vel lacus vitae felis vestibulum volutpat. Etiam est nunc, venenatis in, tristique eu, imperdiet ac, nisl. Cum sociis natoque penatibus et magnis dis parturient montes, nascetur ridiculus mus. In iaculis facilisis massa. Etiam eu urna. Sed porta. Suspendisse quam leo, molestie sed, luctus quis, feugiat in, pede. Fusce tellus. Sed metus augue, convallis et, vehicula ut, pulvinar eu, ante. Integer orci tellus, tristique vitae, consequat nec, porta vel, lectus.</p>
  <p>Nulla sit amet diam. Duis non nunc. Nulla rhoncus dictum metus. Curabitur tristique mi condimentum orci. Phasellus pellentesque aliquam enim. Proin dui lectus, cursus eu, mattis laoreet, viverra sit amet, quam. Curabitur vel dolor ultrices ipsum dictum tristique. Praesent vitae lacus. Ut velit enim, vestibulum non, fermentum nec, hendrerit quis, leo.</p>
</section>
<a class="abs pill pill-or viewall-1" href="#">View all</a>

<h2 class="abs h2 best-title">Best Selling Products</h2>
<div class="abs thumbs">
  <div class="thumb"><div role="img" aria-label="Photo of dried apricots and prunes" style="background:linear-gradient(135deg,#e89a3a,#3a2418)"></div></div>
  <div class="thumb"><div role="img" aria-label="Photo of a cup of tea" style="background:radial-gradient(circle,#e8a030,#9a5a10)"></div></div>
  <div class="thumb"><div role="img" aria-label="Photo of chocolate dipped dried fruit" style="background:linear-gradient(135deg,#f2ece4,#4a2a18)"></div></div>
  <div class="thumb"><div role="img" aria-label="Photo of a box of assorted nuts" style="background:linear-gradient(135deg,#d8b07a,#8a6030)"></div></div>
</div>
<a class="abs pill pill-or viewall-2" href="#">View all</a>

<div class="abs rule" style="top:1464px"></div>

<section class="abs col col-1">
  <h3>Quality &amp; Services</h3>
  <div class="ph" role="img" aria-label="Photo of strawberry ice cream scoop" style="background:linear-gradient(135deg,#9a1a2c,#e8b0b0 50%,#f2d8d0)"></div>
  <p class="t">Nulla rhoncus dictum metus.</p>
  <p class="b">Phasellus pellentesque aliquam enim. Proin dui lectus, cursus eu, mattis laoreet, viverra sit amet, quam. Curabitur vel dolor ultrices ipsum dictum tristique. Praesent vitae lacus. Ut velit enim, vestibulum non,</p>
</section>
<section class="abs col col-2">
  <h3>Why Choose Us</h3>
  <div class="ph" role="img" aria-label="Photo of baked snails on a plate" style="background:linear-gradient(135deg,#f4ece2,#c88a4a 50%,#6a3a18)"></div>
  <p class="t">Nulla rhoncus dictum metus.</p>
  <p class="b">Phasellus pellentesque aliquam enim. Proin dui lectus, cursus eu, mattis laoreet, viverra sit amet, quam. Curabitur vel dolor ultrices ipsum dictum tristique. Praesent vitae lacus. Ut velit enim, vestibulum non,</p>
</section>
<section class="abs col col-3 quote">
  <h3>Testimonials</h3>
  <p class="t">Nulla rhoncus dictum metus.</p>
  <p class="b">Phasellus pellentesque aliquam enim. Proin dui lectus, cursus eu, mattis laoreet, viverra sit amet, quam. Curabitur vel dolor ultrices ipsum dictum tristique. Praesent vitae lacus. Ut velit enim, vestibulum non, fermentum nec</p>
  <p class="by">BY AUTHOR NAME</p>
  <p class="t">Nulla rhoncus dictum metus.</p>
  <p class="b">Phasellus pellentesque aliquam enim. Proin dui lectus, cursus eu, mattis laoreet, viverra sit amet, quam. Curabitur vel dolor ultrices ipsum dictum tristique</p>
  <p class="by">BY AUTHOR NAME</p>
</section>
<a class="abs pill pill-y rm-1" href="#">read more</a>
<a class="abs pill pill-y rm-2" href="#">read more</a>
<a class="abs pill pill-y rm-3" href="#">View all</a>

<footer class="abs footer"></footer>
<ul class="abs fcol" style="left:74px"><li>Aryuvedic</li><li>Drinks &amp; mixes</li><li>Dry fruit, nuts &amp; leaves</li><li>Dairy, jaggery &amp; sugars</li><li>Ez-to-make</li><li>Flour &amp; wheat</li></ul>
<ul class="abs fcol" style="left:288px"><li>Kitchenware</li><li>Pooja / religious</li><li>Lentil, dals &amp; beans</li><li>Concerates, sryups &amp; molasses</li><li>Noodles &amp; soups</li><li>Rice</li></ul>
<ul class="abs fcol" style="left:544px"><li>Cosmetics/beauty</li><li>Middle eastern foods</li><li>Sauces &amp; pastes</li><li>Sweets</li><li>Spices</li><li>Papads &amp; snacks</li></ul>
<ul class="abs fcol" style="left:753px"><li>About Company</li><li>All Products</li><li>Why Choose Us</li><li>Locations</li><li>Blog</li><li>Testimonials</li></ul>
<ul class="abs fcol" style="left:946px"><li>Customer Support</li><li>Sitemap</li><li>Shop Now</li><li>Order Now</li><li>My Account</li><li>Contact Us</li></ul>

<svg class="abs ground" width="1200" height="169" viewBox="0 0 1200 169" aria-hidden="true">
  <path d="M0 60 C150 40 260 90 420 80 C600 68 700 30 880 50 C1000 62 1100 40 1200 30 V169 H0 Z" fill="#fdf5c8"/>
</svg>
<div class="abs toy-blocks" role="img" aria-label="Illustration of colourful toy blocks"></div>
<div class="abs toy-horse" role="img" aria-label="Illustration of a toy rocking horse"></div>

<div class="abs copy">© 2012 Company Name.  All right reserved</div>
<div class="abs legal">Term of Use.  Policy Privacy</div>

</body>
</html>
```